Business Card Design

I'd like to have some business cards designed using my new logo. I am an accountant and company secretary and offer these services through Holloway Meridian Advisory Pty Ltd. I am the sole Director of the company. Please let me know if you require any further logo files.

Industry/Entity Type

Business

```html
<!DOCTYPE html>
<html lang="en">
<head>
<meta charset="utf-8">
<title>Holloway Meridian Advisory — Business Card</title>
<link rel="stylesheet" href="https://fonts.googleapis.com/css2?family=Cinzel:wght@400&family=Open+Sans:wght@400;700&display=swap">
<style>
  :root {
    --bg: #6f7a88;
    --card: #ffffff;
    --card-shade: #f1f1f1;
    --grey-light: #9a9b9e;
    --grey-dark: #5f6063;
    --blue: #2361d6;
    --ink: #3a3b3d;
    --ink-soft: #6c6d70;
    --mark: #2361d6;
  }
  * { margin: 0; padding: 0; box-sizing: border-box; }
  html, body { width: 1200px; height: 1024px; overflow: hidden; }
  body {
    background: var(--bg);
    font-family: "Open Sans", sans-serif;
    display: flex;
    flex-direction: column;
    align-items: center;
    justify-content: center;
    gap: 64px;
  }
  .card {
    position: relative;
    width: 700px;
    height: 400px;
    border-radius: 22px;
    overflow: hidden;
    background: linear-gradient(135deg, var(--card) 0%, var(--card-shade) 100%);
    box-shadow: 0 14px 30px rgba(0,0,0,0.28);
  }
  .card .wave { position: absolute; inset: 0; width: 100%; height: 100%; }
  .brand {
    position: absolute;
    display: flex;
    align-items: center;
    gap: 16px;
  }
  .brand-dot {
    width: 46px; height: 46px;
    border-radius: 50%;
    background: var(--mark);
    flex: none;
  }
  .brand-name {
    font-family: "Cinzel", serif;
    font-weight: 400;
    color: var(--ink-soft);
    text-transform: uppercase;
    line-height: 1.05;
    letter-spacing: 0.02em;
  }
  /* front */
  .card-front .brand { left: 70px; top: 150px; }
  .card-front .brand-name { font-size: 22px; }
  .card-front .site {
    position: absolute;
    right: 70px; bottom: 120px;
    color: #fff;
    font-size: 17px;
    letter-spacing: 0.02em;
  }
  /* back */
  .card-back .contacts {
    position: absolute;
    left: 44px; top: 40px;
    list-style: none;
    font-size: 16px;
    color: var(--ink);
    line-height: 1.45;
  }
  .contacts li { display: flex; align-items: center; gap: 10px; }
  .contacts svg { width: 13px; height: 13px; fill: var(--blue); flex: none; }
  .card-back .brand { left: 222px; top: 60px; gap: 14px; }
  .card-back .brand-dot { width: 36px; height: 36px; }
  .card-back .brand-name { font-size: 16px; }
  .card-back .legal {
    position: absolute;
    left: 44px; bottom: 40px;
    font-size: 15px;
    color: var(--ink);
    line-height: 1.5;
  }
  .card-back .person {
    position: absolute;
    right: 36px; bottom: 36px;
    text-align: right;
    color: #fff;
  }
  .person-name { font-size: 22px; font-weight: 700; line-height: 1.3; }
  .person-role { font-size: 15px; }
</style>
</head>
<body>

  <section class="card card-front" aria-label="Card front">
    <svg class="wave" viewBox="0 0 700 400" preserveAspectRatio="none" aria-hidden="true">
      <defs>
        <linearGradient id="greyFront" x1="0" y1="0" x2="1" y2="0">
          <stop offset="0" stop-color="var(--grey-light)"/>
          <stop offset="1" stop-color="var(--grey-dark)"/>
        </linearGradient>
      </defs>
      <path d="M 448 0 C 420 150, 360 260, 300 400 L 700 400 L 700 0 Z" fill="var(--blue)"/>
      <path d="M 466 0 C 440 150, 380 260, 320 400 L 700 400 L 700 0 Z" fill="url(#greyFront)"/>
    </svg>
    <div class="brand">
      <span class="brand-dot"></span>
      <span class="brand-name">Holloway<br>Meridian Advisory<br>Pty Ltd</span>
    </div>
    <p class="site">www.hma.com.au</p>
  </section>

  <section class="card card-back" aria-label="Card back">
    <svg class="wave" viewBox="0 0 700 400" preserveAspectRatio="none" aria-hidden="true">
      <defs>
        <linearGradient id="greyBack" x1="0" y1="0" x2="1" y2="0">
          <stop offset="0" stop-color="var(--grey-light)"/>
          <stop offset="1" stop-color="var(--grey-dark)"/>
        </linearGradient>
      </defs>
      <path d="M 450 0 C 480 120, 600 200, 420 400 L 700 400 L 700 0 Z" fill="var(--blue)"/>
      <path d="M 470 0 C 500 120, 620 200, 440 400 L 700 400 L 700 0 Z" fill="url(#greyBack)"/>
    </svg>
    <ul class="contacts">
      <li><svg viewBox="0 0 24 24"><path d="M6.6 10.8a15 15 0 0 0 6.6 6.6l2.2-2.2c.3-.3.7-.4 1-.2 1.1.4 2.3.6 3.6.6.6 0 1 .4 1 1V20c0 .6-.4 1-1 1A17 17 0 0 1 3 4c0-.6.4-1 1-1h3.5c.6 0 1 .4 1 1 0 1.3.2 2.5.6 3.6.1.3 0 .7-.2 1z"/></svg>0412630518</li>
      <li><svg viewBox="0 0 24 24"><rect x="6" y="2" width="12" height="20" rx="2"/></svg>0412630518</li>
      <li><svg viewBox="0 0 24 24"><path d="M2 5h20v14H2z M2 5l10 8 10-8" /></svg>info@hma.com.au</li>
      <li><svg viewBox="0 0 24 24"><circle cx="12" cy="12" r="10"/></svg>www.hma.com.au</li>
    </ul>
    <div class="brand">
      <span class="brand-dot"></span>
      <span class="brand-name">Holloway<br>Meridian Advisory<br>Pty Ltd</span>
    </div>
    <div class="legal">
      <p>Ashfield 6054</p>
      <p>ABN: 38 274 816 502 &nbsp;ACN: 274 816 502</p>
    </div>
    <div class="person">
      <p class="person-name">Daniel Reyes</p>
      <p class="person-role">Director</p>
    </div>
  </section>

</body>
</html>
```